QUIVL Systems website

We need a website design using much of the information on the QUIVL flyer (attached) we just had a PixelMarsh designer create. We'd like a WordPress Site, no need for a shopping cart attached to it. It should have an About us page, Book titles page, a blog page, Membership and Navigators pages contact us and privacy policy and terms of services.

Coding

Coded - Design and coding required

```html
<!DOCTYPE html>
<html lang="en">
<head>
<meta charset="utf-8">
<title>QUIVL Systems</title>
<link href="https://fonts.googleapis.com/css2?family=Roboto:wght@400;500;700;900&family=Open+Sans:wght@400;600&display=swap" rel="stylesheet">
<style>
:root{
  --navy:#253f73;
  --ink:#222428;
  --body:#555a60;
  --white:#ffffff;
  --pale:#edf2f9;
  --line:#d8dbe0;
  --footer:#1b1b1b;
  --footer-text:#d7d7d7;
}
*{margin:0;padding:0;box-sizing:border-box}
html,body{width:1200px;height:3797px;overflow:hidden;background:var(--white)}
body{position:relative;font-family:"Open Sans",Arial,sans-serif;color:var(--body)}
.abs{position:absolute}
.heading{font-family:"Roboto",Arial,sans-serif;font-weight:700;color:var(--ink);text-align:center;letter-spacing:.3px}

/* header */
.site-header{left:0;top:0;width:1200px;height:101px;background:var(--white);z-index:3}
.logo-disc{left:72px;top:-48px;width:296px;height:296px;border-radius:50%;background:var(--white);z-index:4}
.logo-name{left:72px;top:82px;width:296px;text-align:center;font-family:"Roboto",Arial,sans-serif;font-weight:700;font-size:58px;color:var(--navy);letter-spacing:2px;z-index:5}
.top-contact{right:100px;top:16px;font-family:"Roboto",Arial,sans-serif;font-size:15px;font-weight:500;color:var(--ink);display:flex;align-items:center;gap:10px;z-index:5}
.top-contact svg{width:15px;height:15px;fill:var(--navy)}
.main-nav{left:435px;top:62px;width:670px;display:flex;justify-content:space-between;align-items:center;font-family:"Roboto",Arial,sans-serif;font-weight:500;font-size:15px;color:var(--ink);z-index:5}
.main-nav .current{color:var(--navy)}

/* hero */
.hero{left:0;top:101px;width:1200px;height:562px;background:linear-gradient(110deg,#6e7c8c 0%,#a9b3bd 35%,#8d97a3 60%,#5a4f52 100%)}
.hero-title{left:0;top:252px;width:1200px;text-align:center;font-family:"Roboto",Arial,sans-serif;font-weight:700;font-size:64px;line-height:82px;color:var(--white)}
.hero-btn{left:500px;top:450px;width:200px;height:68px;border:2px solid var(--white);border-radius:34px;color:var(--white);font-family:"Roboto",Arial,sans-serif;font-weight:700;font-size:16px;display:flex;align-items:center;justify-content:center}
.hero-dots{left:566px;top:588px;display:flex;gap:4px}
.hero-dots span{width:13px;height:13px;border-radius:50%;border:2px solid var(--white)}
.hero-dots span.on{background:var(--white)}

/* intro */
.intro-title{left:0;top:748px;width:1200px;font-size:40px;line-height:54px}
.intro-text{left:177px;top:884px;width:848px;text-align:center;font-size:14.5px;line-height:30px}
.pillar{width:240px;text-align:center}
.pillar svg{display:block;margin:0 auto}
.pillar h3{font-family:"Roboto",Arial,sans-serif;font-weight:700;font-size:20px;color:var(--ink);margin-top:34px}
.pillar p{font-size:14.5px;line-height:25px;margin-top:10px}
.arrow{top:1186px;width:20px;height:34px}

/* membership */
.member-band{left:0;top:1400px;width:1200px;height:436px;background:var(--pale)}
.member-title{left:0;top:1480px;width:1200px;font-size:40px;line-height:54px}
.card{top:1641px;width:313px;height:524px;background:var(--white);border:1px solid var(--line);box-shadow:0 1px 4px rgba(0,0,0,.08)}
.card-photo{height:192px}
.card h3{font-family:"Roboto",Arial,sans-serif;font-weight:700;font-size:21px;color:var(--ink);margin:26px 0 0 30px}
.card ul{list-style:none;margin:20px 24px 0 30px}
.card li{position:relative;padding-left:28px;font-size:14px;line-height:22px;margin-bottom:23px}
.card li svg{position:absolute;left:0;top:3px;width:16px;height:16px}
.join-btn{left:511px;top:2221px;width:178px;height:60px;border-radius:30px;background:var(--navy);color:var(--white);font-family:"Roboto",Arial,sans-serif;font-weight:700;font-size:16px;display:flex;align-items:center;justify-content:center}

/* contact */
.contact{left:0;top:2390px;width:1200px;height:481px;background:linear-gradient(100deg,#3e5f93 0%,#2d4f86 45%,#4b6a98 75%,#334f7c 100%)}
.contact-title{left:0;top:2448px;width:1200px;font-size:40px;color:var(--white)}
.field{background:var(--white);font-size:14px;color:#555;padding:10px 12px}
.submit-btn{left:537px;top:2752px;width:126px;height:50px;border:2px solid var(--white);border-radius:25px;color:var(--white);font-family:"Roboto",Arial,sans-serif;font-weight:700;font-size:16px;display:flex;align-items:center;justify-content:center}

/* about */
.about-box{left:99px;top:2967px;width:592px;height:426px;border:2px solid #cfd2d6}
.about-title{left:154px;top:3010px;font-family:"Roboto",Arial,sans-serif;font-weight:700;font-size:38px;color:var(--ink)}
.about-text{left:154px;top:3082px;width:430px;font-size:14.5px;line-height:26.5px}
.read-btn{left:154px;top:3292px;width:142px;height:50px;border:2px solid var(--navy);border-radius:25px;color:var(--navy);font-family:"Roboto",Arial,sans-serif;font-weight:700;font-size:15px;display:flex;align-items:center;justify-content:center}
.video{left:633px;top:3013px;width:466px;height:334px;background:radial-gradient(circle at 70% 40%,#3f5a78 0%,#1d2a3b 55%,#0f1620 100%);box-shadow:0 4px 12px rgba(0,0,0,.3)}
.play{left:838px;top:3150px;width:60px;height:60px;border-radius:50%;background:var(--white)}

/* footer */
.site-footer{left:0;top:3499px;width:1200px;height:298px;background:var(--footer)}
.social{top:3571px;width:48px;height:48px;border-radius:50%;border:2px solid #bdbdbd}
.footer-line{left:0;width:1200px;text-align:center;font-size:14px;color:var(--footer-text);display:flex;justify-content:center;align-items:center;gap:12px}
.footer-line svg{width:14px;height:14px;fill:var(--footer-text)}
</style>
</head>
<body>

<header class="abs site-header"></header>
<div class="abs logo-disc"></div>
<div class="abs logo-name">QUIVL</div>
<div class="abs top-contact">
  <svg viewBox="0 0 24 24"><path d="M6.6 10.8a15 15 0 0 0 6.6 6.6l2.2-2.2c.3-.3.7-.4 1-.2 1.1.4 2.3.6 3.6.6.6 0 1 .4 1 1V20c0 .6-.4 1-1 1A17 17 0 0 1 3 4c0-.6.4-1 1-1h3.5c.6 0 1 .4 1 1 0 1.3.2 2.5.6 3.6.1.3 0 .7-.2 1z"/></svg>
  <span>833-555-0147</span><span>|</span>
  <svg viewBox="0 0 24 24"><path d="M2 5h20v14H2z M2 5l10 8 10-8" fill="none" stroke="#253f73" stroke-width="2.5"/></svg>
  <span>info@quivl1.com</span>
</div>
<nav class="abs main-nav">
  <span class="current">HOME</span><span>ABOUT US</span><span>BOOK TITLES</span><span>BLOG</span><span>MEMBERSHIP</span><span>CONTACT US</span>
  <svg width="16" height="16" viewBox="0 0 24 24"><circle cx="10" cy="10" r="7" fill="none" stroke="#222428" stroke-width="3"/><path d="M15 15l7 7" stroke="#222428" stroke-width="3"/></svg>
</nav>

<section>
  <div class="abs hero" role="img" aria-label="Photo of a businesswoman working at a glass board with charts"></div>
  <h1 class="abs hero-title">ACCELERATE YOUR<br>BUSINESS WITH QUIVL™!</h1>
  <div class="abs hero-btn">GET MORE INFO</div>
  <div class="abs hero-dots"><span class="on"></span><span></span><span></span><span></span></div>
</section>

<section>
  <h2 class="abs heading intro-title">CREATED BY ENTREPRENEURS<br>FOR ENTREPRENEURS</h2>
  <p class="abs intro-text">A team of 7 successful entrepreneurs put their heads together in an effort to help improve the statistics on how many small businesses succeed. After tapping into the great minds of business thought leaders* from around the globe, they developed the first comprehensive program for small businesses (up to $5M revenues) and packaged it into a simple, affordable, sustainable membership model. And QUIVL was born!</p>

  <svg class="abs arrow" style="left:38px" viewBox="0 0 20 34"><path d="M17 2L3 17l14 15" fill="none" stroke="#777" stroke-width="3"/></svg>
  <svg class="abs arrow" style="left:1142px" viewBox="0 0 20 34"><path d="M3 2l14 15L3 32" fill="none" stroke="#777" stroke-width="3"/></svg>

  <div class="abs pillar" style="left:62px;top:1045px">
    <svg width="152" height="152" viewBox="0 0 152 152"><circle cx="76" cy="76" r="74" fill="none" stroke="#333" stroke-width="3"/><circle cx="76" cy="76" r="64" fill="#f2f2f2"/><circle cx="76" cy="76" r="28" fill="none" stroke="#253f73" stroke-width="5"/><circle cx="76" cy="76" r="16" fill="none" stroke="#253f73" stroke-width="5"/><circle cx="76" cy="76" r="6" fill="#253f73"/></svg>
    <h3>STRATEGY</h3><p>Long-Term Vision,Tactical<br>Planning</p>
  </div>
  <div class="abs pillar" style="left:341px;top:1045px">
    <svg width="152" height="152" viewBox="0 0 152 152"><circle cx="76" cy="76" r="74" fill="none" stroke="#333" stroke-width="3"/><circle cx="76" cy="76" r="64" fill="#f2f2f2"/><g fill="#253f73"><circle cx="76" cy="60" r="10"/><path d="M60 94c0-14 7-22 16-22s16 8 16 22z"/><circle cx="53" cy="66" r="8"/><path d="M40 94c0-11 5-18 13-18 3 0 5 1 7 3-3 4-4 9-4 15z"/><circle cx="99" cy="66" r="8"/><path d="M112 94c0-11-5-18-13-18-3 0-5 1-7 3 3 4 4 9 4 15z"/></g></svg>
    <h3>TEAM</h3><p>Healthy Team Relationships<br>&amp; Development</p>
  </div>
  <div class="abs pillar" style="left:617px;top:1045px">
    <svg width="152" height="152" viewBox="0 0 152 152"><circle cx="76" cy="76" r="74" fill="none" stroke="#333" stroke-width="3"/><circle cx="76" cy="76" r="64" fill="#f2f2f2"/><g fill="#253f73"><circle cx="66" cy="82" r="16"/><g stroke="#253f73" stroke-width="8"><path d="M66 58v48M42 82h48M49 65l34 34M83 65L49 99"/></g><circle cx="66" cy="82" r="6" fill="#f2f2f2"/><circle cx="94" cy="58" r="10"/><g stroke="#253f73" stroke-width="5"><path d="M94 43v30M79 58h30M84 48l20 20M104 48L84 68"/></g><circle cx="94" cy="58" r="4" fill="#f2f2f2"/></g></svg>
    <h3>ACTION</h3><p>Processes to Execute<br>the Vision</p>
  </div>
  <div class="abs pillar" style="left:893px;top:1045px">
    <svg width="152" height="152" viewBox="0 0 152 152"><circle cx="76" cy="76" r="74" fill="none" stroke="#333" stroke-width="3"/><circle cx="76" cy="76" r="64" fill="#f2f2f2"/><g fill="#253f73"><circle cx="76" cy="62" r="14"/><path d="M52 98c0-16 10-24 24-24s24 8 24 24z"/></g></svg>
    <h3>ACCOUNTABILITY</h3><p>Tools and Checklists<br>to Stay on Track</p>
  </div>
</section>

<section>
  <div class="abs member-band"></div>
  <h2 class="abs heading member-title">BECOME A QUIVL MEMBER TODAY<br>AND YOU WILL RECEIVE...</h2>

  <article class="abs card" style="left:96px">
    <div class="card-photo" role="img" aria-label="Photo of a coach presenting to a small team" style="background:linear-gradient(120deg,#8b9aa8,#d6d9dc 50%,#6f7983)"></div>
    <h3>QUIVL™ COACHING</h3>
    <ul>
      <li><svg viewBox="0 0 16 16"><circle cx="8" cy="8" r="8" fill="#253f73"/><path d="M4.5 8.2l2.3 2.3 4.7-4.8" fill="none" stroke="#fff" stroke-width="1.8"/></svg>Coaching for you and your leadership team</li>
      <li><svg viewBox="0 0 16 16"><circle cx="8" cy="8" r="8" fill="#253f73"/><path d="M4.5 8.2l2.3 2.3 4.7-4.8" fill="none" stroke="#fff" stroke-width="1.8"/></svg>Launch pad, monthly and quarterly touchpoints, annual planning</li>
      <li><svg viewBox="0 0 16 16"><circle cx="8" cy="8" r="8" fill="#253f73"/><path d="M4.5 8.2l2.3 2.3 4.7-4.8" fill="none" stroke="#fff" stroke-width="1.8"/></svg>Continuous learning mode</li>
      <li><svg viewBox="0 0 16 16"><circle cx="8" cy="8" r="8" fill="#253f73"/><path d="M4.5 8.2l2.3 2.3 4.7-4.8" fill="none" stroke="#fff" stroke-width="1.8"/></svg>All QUIVL coaches are successful million-dollar entrepreneurs</li>
    </ul>
  </article>

  <article class="abs card" style="left:443px">
    <div class="card-photo" role="img" aria-label="Photo of hands working together over a table of papers" style="background:linear-gradient(120deg,#4a4038,#b7aa98 50%,#5c5147)"></div>
    <h3>QUIVL™ STRUCTURE</h3>
    <ul>
      <li><svg viewBox="0 0 16 16"><circle cx="8" cy="8" r="8" fill="#253f73"/><path d="M4.5 8.2l2.3 2.3 4.7-4.8" fill="none" stroke="#fff" stroke-width="1.8"/></svg>Structured program that ensures focus, productivity and accountability.</li>
      <li><svg viewBox="0 0 16 16"><circle cx="8" cy="8" r="8" fill="#253f73"/><path d="M4.5 8.2l2.3 2.3 4.7-4.8" fill="none" stroke="#fff" stroke-width="1.8"/></svg>Robust collection of simple, streamlined tools and processes</li>
      <li><svg viewBox="0 0 16 16"><circle cx="8" cy="8" r="8" fill="#253f73"/><path d="M4.5 8.2l2.3 2.3 4.7-4.8" fill="none" stroke="#fff" stroke-width="1.8"/></svg>QUIVL Strategy Stack – for clarity and alignment</li>
    </ul>
  </article>

  <article class="abs card" style="left:785px">
    <div class="card-photo" role="img" aria-label="Photo of a laptop and documents on a desk" style="background:linear-gradient(120deg,#d9dfe4,#8fb7c8 55%,#4fa6c0)"></div>
    <h3>QUIVL™ RESOURCES</h3>
    <ul>
      <li><svg viewBox="0 0 16 16"><circle cx="8" cy="8" r="8" fill="#253f73"/><path d="M4.5 8.2l2.3 2.3 4.7-4.8" fill="none" stroke="#fff" stroke-width="1.8"/></svg>Pre-packaged business processes</li>
      <li><svg viewBox="0 0 16 16"><circle cx="8" cy="8" r="8" fill="#253f73"/><path d="M4.5 8.2l2.3 2.3 4.7-4.8" fill="none" stroke="#fff" stroke-width="1.8"/></svg>Simplified business templates and forms</li>
      <li><svg viewBox="0 0 16 16"><circle cx="8" cy="8" r="8" fill="#253f73"/><path d="M4.5 8.2l2.3 2.3 4.7-4.8" fill="none" stroke="#fff" stroke-width="1.8"/></svg>Online, self-paced learning library</li>
      <li><svg viewBox="0 0 16 16"><circle cx="8" cy="8" r="8" fill="#253f73"/><path d="M4.5 8.2l2.3 2.3 4.7-4.8" fill="none" stroke="#fff" stroke-width="1.8"/></svg>Technology platform for tracking and accountability</li>
    </ul>
  </article>

  <div class="abs join-btn">JOIN US NOW!</div>
</section>

<section>
  <div class="abs contact" role="img" aria-label="Photo of a blue-toned office with people at desks"></div>
  <h2 class="abs heading contact-title">GET IN TOUCH</h2>
  <div class="abs field" style="left:258px;top:2537px;width:334px;height:41px">First Name</div>
  <div class="abs field" style="left:605px;top:2537px;width:334px;height:41px">Last Name</div>
  <div class="abs field" style="left:258px;top:2590px;width:334px;height:41px">Email Address</div>
  <div class="abs field" style="left:605px;top:2590px;width:334px;height:41px">Phone Number</div>
  <div class="abs field" style="left:258px;top:2643px;width:681px;height:81px">Message</div>
  <div class="abs submit-btn">SUBMIT</div>
</section>

<section>
  <div class="abs about-box"></div>
  <h2 class="abs about-title">ABOUT QUIVL</h2>
  <p class="abs about-text">A team of 7 successful entrepreneurs put their heads together in an effort to help improve the statistics on how many small businesses succeed. After tapping into the great minds of business thought leaders* from around the globe, they developed the first comprehensive program for small businesses (up to $5M revenues) and packaged it into a simple, affordable, sustainable membership model. And QUIVL was born!</p>
  <div class="abs read-btn">READ MORE</div>
  <div class="abs video" role="img" aria-label="Video still of a man working at a computer in a dark office"></div>
  <div class="abs play"><svg width="60" height="60" viewBox="0 0 60 60"><path d="M24 18l18 12-18 12z" fill="#111"/></svg></div>
</section>

<footer>
  <div class="abs site-footer"></div>
  <div class="abs social" style="left:482px"></div>
  <div class="abs social" style="left:541px"></div>
  <div class="abs social" style="left:599px"></div>
  <div class="abs social" style="left:657px"></div>
  <div class="abs footer-line" style="top:3656px">
    <svg viewBox="0 0 24 24"><path d="M12 2a7 7 0 0 0-7 7c0 5 7 13 7 13s7-8 7-13a7 7 0 0 0-7-7zm0 9.5A2.5 2.5 0 1 1 12 6.5a2.5 2.5 0 0 1 0 5z"/></svg>
    <span>418 Maple Crest Dr Fairview Hollow, MO 63090</span><span>|</span>
    <svg viewBox="0 0 24 24"><path d="M6.6 10.8a15 15 0 0 0 6.6 6.6l2.2-2.2c.3-.3.7-.4 1-.2 1.1.4 2.3.6 3.6.6.6 0 1 .4 1 1V20c0 .6-.4 1-1 1A17 17 0 0 1 3 4c0-.6.4-1 1-1h3.5c.6 0 1 .4 1 1 0 1.3.2 2.5.6 3.6.1.3 0 .7-.2 1z"/></svg>
    <span>833-555-0147</span><span>|</span>
    <svg viewBox="0 0 24 24"><path d="M2 5h20v14H2z" /><path d="M2 5l10 8 10-8" fill="none" stroke="#1b1b1b" stroke-width="2"/></svg>
    <span>info@quivl1.com</span>
  </div>
  <div class="abs footer-line" style="top:3694px;gap:16px">
    <span>Help</span><span>|</span><span>FAQ</span><span>|</span><span>Support</span><span>|</span><span>Sitemap</span><span>|</span><span>Terms of Service</span><span>|</span><span>Privacy Policy</span>
  </div>
  <div class="abs footer-line" style="top:3730px">QUIVL Systems © 2018 All rights reserved.</div>
</footer>

</body>
</html>
```